LOS PINOS DE ARENA - EXCLUSIVE AND LUXURY REAL ESTATE PROJECT

Se trata del diseño de un mono poste grande (4 m x 2 m) o (8m x 3m) anunciando la construcción de 30 villas de lujo en un terreno en primera línea de playa en el sur de España (Cádiz).

La idea es crear expectación y transmitir lujo y exclusividad.

Target Market(s)

Clientes de alto poder adquisitivo que quieran adquirir su segunda vivienda en un entorno privilegiado a escasos pasos de una de las playas más bonitas de Cádiz.

Industry/Entity Type

REAL ESTATE

Colors

Designer to choose colors to be used in the design.

Requirements
Must have
• LOS PINOS DE ARENA as the name of the development
Nice to have
• Crear expectación con ideas del tipo: “Coming soon” o “No te lo puedes perder”

```html
<!DOCTYPE html>
<html lang="es">
<head>
<meta charset="utf-8">
<title>Los Pinos de Arena – Coming Soon</title>
<link rel="stylesheet" href="https://fonts.googleapis.com/css2?family=Bebas+Neue&family=Poppins:wght@700;800&display=swap">
<style>
  :root {
    --page: #ffffff;
    --navy: #143f94;
    --green: #00fa7c;
    --white: #f7f8f8;
    --sky-top: #3b66b4;
    --sky-mid: #6f9bd0;
    --stone: #c9c6b6;
    --pool: #46c3dc;
    --deck: #8a6548;
    --deck-dark: #6d4c35;
  }
  * { box-sizing: border-box; margin: 0; padding: 0; }
  html, body {
    width: 922px; height: 1200px; overflow: hidden;
    background: var(--page);
  }
  .billboard {
    position: absolute;
    left: 31px; top: 385px;
    width: 860px; height: 429px;
    background: var(--white);
    box-shadow: 0 2px 6px rgba(0,0,0,0.25);
    overflow: hidden;
  }
  .villa-photo {
    position: absolute; left: 0; top: 0;
    width: 640px; height: 100%;
    background: linear-gradient(180deg,
      var(--sky-top) 0%, var(--sky-mid) 22%,
      #e9ecee 40%, var(--stone) 52%,
      var(--pool) 64%, var(--deck) 74%, var(--deck-dark) 100%);
  }
  .headline-panel {
    position: absolute;
    left: 448px; top: 24px;
    width: 386px; height: 379px;
    background: var(--navy);
    border-radius: 14px;
    display: flex; flex-direction: column; align-items: center;
    text-align: center;
  }
  .project-name {
    margin-top: 14px;
    line-height: 1;
  }
  .project-name__top {
    display: block;
    font-family: 'Bebas Neue', sans-serif;
    font-size: 96px;
    line-height: 0.84;
    color: var(--green);
    letter-spacing: 1px;
  }
  .project-name__bottom {
    display: block;
    font-family: 'Poppins', sans-serif;
    font-weight: 700;
    font-size: 58px;
    line-height: 1;
    color: var(--white);
    letter-spacing: -2px;
    margin-top: 2px;
  }
  .divider {
    width: 260px; height: 2px; margin-top: 20px;
    background: linear-gradient(90deg, rgba(0,250,124,0), var(--green) 50%, rgba(0,250,124,0));
  }
  .teaser {
    margin-top: 18px;
    font-family: 'Poppins', sans-serif;
    font-weight: 800;
    line-height: 0.9;
  }
  .teaser__coming {
    display: block;
    font-size: 56px;
    color: var(--green);
    letter-spacing: -1px;
  }
  .teaser__soon {
    display: block;
    font-size: 90px;
    letter-spacing: -4px;
  }
  .teaser__soon .accent { color: var(--green); }
  .teaser__soon .light { color: var(--white); }
</style>
</head>
<body>
  <section class="billboard">
    <div class="villa-photo" role="img" aria-label="Modern white luxury villa with pool, stone wall and wooden deck under blue sky"></div>
    <div class="headline-panel">
      <h1 class="project-name">
        <span class="project-name__top">LOS PINOS</span>
        <span class="project-name__bottom">DE ARENA</span>
      </h1>
      <div class="divider"></div>
      <p class="teaser">
        <span class="teaser__coming">COMING</span>
        <span class="teaser__soon"><span class="accent">S</span><span class="light">OO</span><span class="accent">N</span></span>
      </p>
    </div>
  </section>
</body>
</html>
```